Business Card front and back

I am looking for business card design. I really really like the design file I uploaded named 627788_19250069_3478263_85f427ee_image

Target Market(s)

Corporate Fitness High end Private country club

Industry/Entity Type

Fitness Industry

Contact Information for Business Card

The last image I like as an example I uploaded a bunch of my logos. The file labeled "the signature" is my business card information for you to use

Colors
0054AA
0677BA
7BADD7
CADEEF
E8F1F8

Requirements
Must have
• E-mail sigThe file I uploaded labeled "627788_19250069_3478263_85f427ee_image" with all the plus signs on the back if those could be the logo symbol I uploaded labeled "1 back.png"

```html
<!DOCTYPE html>
<html lang="en">
<head>
<meta charset="utf-8">
<title>Stride Works — Business Card Front and Back</title>
<link rel="stylesheet" href="https://fonts.googleapis.com/css2?family=Exo+2:wght@400;700&family=Ubuntu:wght@400&display=swap">
<style>
  :root {
    --page-bg: #1b1b1c;
    --card-bg: #2f2f30;
    --pattern-light: #8a8a8c;
    --pattern-mid: #3c3c3e;
    --pattern-dark: #050506;
    --brand-blue: #3a7fcf;
    --text-white: #f4f4f4;
    --photo-tone-a: #6b5648;
    --photo-tone-b: #1f1f20;
    --symbol-tone-a: #3c3c3e;
    --symbol-tone-b: #050506;
  }
  * { box-sizing: border-box; margin: 0; padding: 0; }
  html, body { width: 1200px; height: 1015px; overflow: hidden; }
  body {
    background: var(--page-bg);
    position: relative;
    font-family: "Ubuntu", sans-serif;
  }
  .card {
    position: absolute;
    width: 560px;
    height: 320px;
    background: var(--card-bg);
    overflow: hidden;
    box-shadow: 0 10px 30px rgba(0,0,0,.5);
  }
  .card--front { left: 90px; top: 110px; }
  .card--back  { left: 550px; top: 580px; }

  .tile-pattern { position: absolute; inset: 0; width: 560px; height: 320px; }

  .brand-lockup {
    position: absolute; left: 0; right: 0; top: 136px;
    display: flex; justify-content: center; align-items: center; gap: 12px;
  }
  .brand-lockup__mark { width: 18px; height: 18px; background: var(--brand-blue); }
  .brand-lockup__name {
    font-family: "Exo 2", sans-serif; font-weight: 700;
    font-size: 30px; letter-spacing: 4px; color: var(--text-white);
    text-transform: uppercase;
    background: var(--card-bg);
    padding: 2px 10px;
  }

  .portrait {
    position: absolute; left: 50px; top: 22px;
    width: 130px; height: 130px; border-radius: 50%;
    border: 3px solid #3d3d3f;
    background: radial-gradient(circle at 50% 40%, var(--photo-tone-a), var(--photo-tone-b) 75%);
  }
  .symbol-large {
    position: absolute; right: 30px; top: 40px;
    width: 250px; height: 240px; border-radius: 30px;
    background: linear-gradient(160deg, var(--symbol-tone-a), var(--symbol-tone-b));
  }
  .person { position: absolute; left: 58px; top: 164px; }
  .person__name {
    font-family: "Exo 2", sans-serif; font-weight: 700;
    font-size: 24px; color: var(--brand-blue); letter-spacing: 1px; line-height: 1;
  }
  .person__role { font-size: 15px; line-height: 18px; color: var(--text-white); margin-top: 2px; }
  .contact-list { list-style: none; margin-top: 8px; }
  .contact-list li {
    display: flex; align-items: center; gap: 8px;
    font-size: 14px; color: var(--text-white); line-height: 21px;
  }
  .contact-list svg { width: 14px; height: 14px; fill: var(--brand-blue); flex: none; }
</style>
</head>
<body>
  <section class="card card--front" aria-label="Card front">
    <svg class="tile-pattern" viewBox="0 0 560 320" role="img" aria-label="Repeating tile pattern fading from light to dark">
      <defs>
        <linearGradient id="tile-shade" x1="1" y1="0" x2="0" y2="1">
          <stop offset="0" stop-color="var(--pattern-light)"/>
          <stop offset=".5" stop-color="var(--pattern-mid)"/>
          <stop offset="1" stop-color="var(--pattern-dark)"/>
        </linearGradient>
        <pattern id="tile-grid" width="70" height="64" patternUnits="userSpaceOnUse" x="12" y="10">
          <rect x="0" y="0" width="46" height="40" rx="8" fill="#fff"/>
        </pattern>
        <mask id="tile-mask">
          <rect width="560" height="320" fill="url(#tile-grid)"/>
        </mask>
      </defs>
      <rect width="560" height="320" fill="url(#tile-shade)" mask="url(#tile-mask)"/>
    </svg>
    <div class="brand-lockup">
      <span class="brand-lockup__mark"></span>
      <span class="brand-lockup__name">Stride Works</span>
    </div>
  </section>

  <section class="card card--back" aria-label="Card back">
    <div class="portrait" role="img" aria-label="Portrait photo of the consultant"></div>
    <div class="symbol-large" role="img" aria-label="Large brand symbol decoration"></div>
    <div class="person">
      <p class="person__name">DANA HOLT</p>
      <p class="person__role">Consultant</p>
      <ul class="contact-list">
        <li><svg viewBox="0 0 24 24"><path d="M6.6 10.8a15 15 0 0 0 6.6 6.6l2.2-2.2c.3-.3.7-.4 1-.2 1.1.4 2.3.6 3.6.6.6 0 1 .4 1 1V20c0 .6-.4 1-1 1A17 17 0 0 1 3 4c0-.6.4-1 1-1h3.5c.6 0 1 .4 1 1 0 1.3.2 2.5.6 3.6.1.3 0 .7-.2 1z"/></svg>555-014-0199</li>
        <li><svg viewBox="0 0 24 24"><path d="M2 5h20v14H2zM3 6l9 7 9-7v-.5H3z"/></svg>dana@strideworks.co</li>
        <li><svg viewBox="0 0 24 24"><path d="M12 2a10 10 0 1 0 0 20 10 10 0 0 0 0-20zm6.9 9h-3a15 15 0 0 0-1.3-6A8 8 0 0 1 18.9 11zM12 4c.9 1.2 1.7 3.7 1.9 7h-3.8c.2-3.3 1-5.8 1.9-7zM4.1 13h3a15 15 0 0 0 1.3 6A8 8 0 0 1 4.1 13zm3-2h-3a8 8 0 0 1 4.3-6 15 15 0 0 0-1.3 6zm3 2h3.8c-.2 3.3-1 5.8-1.900 7-.9-1.2-1.7-3.7-1.9-7zm5.5 6a15 15 0 0 0 1.3-6h3a8 8 0 0 1-4.3 6z"/></svg>www.strideworks.co</li>
        <li><svg viewBox="0 0 24 24"><path d="M12 2a7 7 0 0 0-7 7c0 5 7 13 7 13s7-8 7-13a7 7 0 0 0-7-7zm0 9.5a2.5 2.5 0 1 1 0-5 2.5 2.5 0 0 1 0 5z"/></svg>Lakeshore Region</li>
      </ul>
    </div>
  </section>
</body>
</html>
```